WEEKLY INFORMATIONAL GARDENING NEWSLETTER

New Weekly Email Newsletter needs a banner that reflects company logos, author photo for new Email Campaign using Mail Chimp.

I have attached author photo, as well as our company logos.

The tile of Newsletter should read Tom's Garden Notes. Company colors are black, lime green, white for SodCraft. Colors for sister company, Verdant Mist are black, blue, green as depicted in logos attached. Logos should be on black background. I have attached a photo of the template we are considering using in mail chimp for your reference.

If you have any questions or need additional photos please let me know. Look forward to seeing your designs!

Target Market(s)

Current Clients, potential leads

Industry/Entity Type

Landscape Gardening

Font styles to use
Serif

Colors
9bcb3c
000000

Requirements
Must have
• Colors chosen below, cut out of photo, more life like than picture frame.
• Both company logos
Nice to have
• logos incorporated, as well as author photo.
Should not have
• Sales Pitch, should not have photo in frame.

```html
<!DOCTYPE html>
<html lang="en">
<head>
<meta charset="utf-8">
<title>Tom's Garden Notes</title>
<link rel="stylesheet" href="https://fonts.googleapis.com/css2?family=Josefin+Sans:wght@400;600&family=Josefin+Slab:wght@400&display=swap">
<style>
  :root {
    --ink: #000000;
    --paper: #ffffff;
    --lime: #9bcb3c;
    --slate: #4a4a4a;
    --mist-blue: #2f8fd0;
    --photo-dark: #161412;
    --photo-warm: #7a5442;
    --photo-mid: #3a302a;
  }
  * { margin: 0; padding: 0; box-sizing: border-box; }
  html, body {
    width: 1200px;
    height: 482px;
    overflow: hidden;
    background: var(--paper);
  }
  .banner {
    position: relative;
    width: 1200px;
    height: 482px;
    background: var(--paper);
    overflow: hidden;
  }
  .masthead {
    position: absolute;
    left: 0; top: 0;
    width: 1200px;
    height: 388px;
    background: var(--ink);
  }
  .title-name {
    position: absolute;
    left: 78px;
    top: 76px;
    font-family: "Josefin Slab", serif;
    font-weight: 400;
    font-size: 186px;
    line-height: 1;
    letter-spacing: 4px;
    color: var(--paper);
    white-space: nowrap;
  }
  .title-sub {
    position: absolute;
    left: 82px;
    top: 236px;
    font-family: "Josefin Sans", sans-serif;
    font-weight: 400;
    font-size: 60px;
    line-height: 1;
    letter-spacing: 4px;
    color: var(--lime);
    white-space: nowrap;
  }
  .author-photo {
    position: absolute;
    left: 800px;
    top: 0;
    width: 400px;
    height: 388px;
    border-radius: 48% 0 0 0 / 40% 0 0 0;
    background: linear-gradient(180deg, var(--photo-dark) 0%, var(--photo-mid) 30%, var(--photo-warm) 55%, var(--photo-mid) 80%, var(--photo-dark) 100%);
  }
  .partners {
    position: absolute;
    left: 0; top: 388px;
    width: 1200px;
    height: 94px;
    display: flex;
    align-items: center;
    justify-content: flex-end;
    gap: 50px;
    padding-right: 30px;
  }
  .partner {
    display: flex;
    align-items: center;
    gap: 12px;
    font-family: "Josefin Sans", sans-serif;
    font-weight: 600;
    font-size: 34px;
    line-height: 1;
    letter-spacing: 1px;
    white-space: nowrap;
  }
  .partner-sodcraft { color: var(--slate); }
  .partner-verdant { color: var(--mist-blue); }
  .partner-dot {
    width: 22px;
    height: 22px;
    border-radius: 50%;
    background: var(--lime);
  }
</style>
</head>
<body>
  <div class="banner">
    <header class="masthead">
      <h1 class="title-name">TOM'S</h1>
      <p class="title-sub">GARDEN NOTES</p>
      <div class="author-photo" role="img" aria-label="Author photo"></div>
    </header>
    <footer class="partners">
      <div class="partner partner-sodcraft">SodCraft</div>
      <div class="partner partner-verdant"><span class="partner-dot"></span>Verdant Mist</div>
    </footer>
  </div>
</body>
</html>
```